Create a website for a car broker/car buyers advocate

build a website to suit a car brokering/car buying service. The design should communicate saving people time, money and stress by outsourcing the purchasing process for thier new car. I woudl like a modern site which is scroll able all on one page and wouldnt mind a dark or minimalistic theme. i have uploaded the logo which has also been designed by pixel harbor

Target Market(s)

general consumers, new car buyers, car collectors

Industry/Entity Type

Car Dealer

Font styles to use
Sans Serif

Colors

Designer to choose colors to be used in the design.

Requirements
Must have
• single page scrollable site
• modern design
• professional but fun
Nice to have
• some websites i like of similar businesses are :
• http://www.motorvane.com.au/
• https://drivelumen.com.au/

```html
<!DOCTYPE html>
<html lang="en">
<head>
<meta charset="utf-8">
<title>Velo Brokers – Car Brokering &amp; Car Buying Service</title>
<link href="https://fonts.googleapis.com/css2?family=Mulish:wght@400;600;700;800&family=Open+Sans:wght@400;600&display=swap" rel="stylesheet">
<style>
:root{
  --navy:#3f4a6b;
  --blue:#536aa0;
  --blue-dark:#3d5186;
  --orange:#c4461b;
  --orange-deep:#a8381a;
  --pale:#e4e9f3;
  --ink:#1d1f26;
  --text:#333a47;
  --white:#ffffff;
  --muted:#6b7080;
}
*{margin:0;padding:0;box-sizing:border-box}
html,body{width:1200px;height:3551px;overflow:hidden}
body{position:relative;background:var(--white);font-family:'Open Sans',sans-serif;color:var(--text)}
.abs{position:absolute}
h1,h2,h3,h4,.nav,.btn{font-family:'Mulish',sans-serif}

/* header */
.site-header{position:absolute;left:0;top:0;width:1200px;height:91px;background:var(--white)}
.brand{position:absolute;left:92px;top:28px;display:flex;align-items:center;gap:12px}
.brand-mark{width:30px;height:30px;background:var(--navy);border-radius:4px}
.brand-name{font-family:'Mulish',sans-serif;font-weight:800;font-size:20px;letter-spacing:4px;color:var(--navy)}
.nav{position:absolute;left:368px;top:35px;display:flex;gap:32px;font-size:15px;font-weight:700;color:var(--ink)}
.phone{position:absolute;left:974px;top:34px;font-family:'Mulish',sans-serif;font-weight:600;font-size:16px;color:var(--blue);display:flex;align-items:center;gap:6px}

/* hero */
.hero{position:absolute;left:0;top:91px;width:1200px;height:661px;overflow:hidden;
  background:linear-gradient(180deg,#5a4a35 0%,#8a6a3d 18%,#6b5a4a 40%,#3e3a3c 70%,#4a2e22 100%)}
.hero-photo{position:absolute;inset:0;background:radial-gradient(ellipse at 22% 38%,rgba(240,170,60,.55),transparent 45%),radial-gradient(ellipse at 70% 55%,rgba(150,155,165,.45),transparent 50%)}
.hero-title{position:absolute;left:0;top:150px;width:1205px;text-align:center;color:var(--white);font-weight:600;font-size:50px;letter-spacing:.5px}
.hero-sub{position:absolute;left:0;top:214px;width:1205px;text-align:center;color:var(--white);font-weight:600;font-size:29px}
.search{position:absolute;left:237px;top:270px;width:740px;height:70px;background:rgba(25,25,30,.75);padding:12px 10px;display:flex;gap:9px}
.select{background:var(--white);height:46px;display:flex;align-items:center;justify-content:space-between;padding:0 14px 0 17px;font-size:15px;color:var(--ink)}
.select svg{width:14px;height:14px}
.btn-search{background:var(--blue);color:var(--white);font-weight:800;font-size:17px;width:144px;height:46px;display:flex;align-items:center;justify-content:center}
.hero-arrow{position:absolute;top:262px;width:58px;height:58px;border-radius:50%;background:rgba(255,255,255,.35);display:flex;align-items:center;justify-content:center}
.hero-edge{position:absolute;left:0;top:0}

/* section titles */
.sec-title{position:absolute;left:0;width:1200px;text-align:center;font-weight:700;color:var(--ink);font-size:36px}
.rule{position:absolute;height:3px;width:62px;background:var(--orange)}

.about-text{position:absolute;left:240px;top:842px;width:725px;text-align:center;font-size:19.5px;line-height:27px;color:var(--text)}

/* diamonds band */
.pale-band{position:absolute;left:0;top:1193px;width:1200px;height:629px;background:var(--pale)}
.diamonds{position:absolute;left:0;top:973px}
.tile{position:absolute;width:444px;text-align:center;color:var(--white)}
.tile h3{font-size:28px;font-weight:800}
.tile p{font-size:13px;line-height:19px;margin-top:16px}
.tile .down{margin:16px auto 0;width:46px;height:46px;border:2px solid var(--white);border-radius:50%;display:flex;align-items:center;justify-content:center}

/* cars */
.car{position:absolute;top:1528px;width:221px;height:203px;background:var(--white);box-shadow:0 2px 4px rgba(0,0,0,.12)}
.car .ph{height:156px}
.car h4{text-align:center;font-size:17px;font-weight:700;color:var(--ink);margin-top:13px}
.slide-arrow{position:absolute}

/* why */
.why{position:absolute;left:0;top:1822px;width:1200px;height:493px;background:var(--blue)}
.why-photo{position:absolute;left:0;top:0;width:700px;height:493px;background:linear-gradient(90deg,#3b4250 0%,#5e6a73 35%,#6b7d8d 62%,rgba(83,106,160,0) 100%)}
.why h2{position:absolute;left:672px;top:72px;color:var(--white);font-size:32px;font-weight:700}
.why .rule{background:var(--white);left:672px;top:115px;width:80px}
.why-text{position:absolute;left:672px;top:132px;width:410px;color:var(--white);font-size:14.5px;line-height:19.5px}
.feature{position:absolute;display:flex;align-items:center;gap:9px;color:var(--white);font-family:'Mulish',sans-serif;font-weight:700;font-size:15px;line-height:18px}
.feature .ic{width:36px;height:36px;border-radius:50%;background:#35405e;display:flex;align-items:center;justify-content:center}

/* blogs */
.blogs-title{position:absolute;left:156px;top:2370px;font-size:33px;font-weight:700;color:var(--navy)}
.blog{position:absolute;top:2451px;width:284px;height:353px;border:1px solid #c9cdd6;background:var(--white)}
.blog .ph{height:165px}
.blog h4{margin:27px 22px 0;font-size:17px;line-height:19px;color:var(--blue);font-weight:600}
.blog p{margin:10px 22px 0;font-size:12.5px;line-height:17px;color:var(--muted)}
.btn-read{position:absolute;left:22px;top:300px;width:112px;height:30px;background:var(--blue);color:var(--white);font-size:13px;font-weight:700;display:flex;align-items:center;justify-content:center}

/* testimonials */
.testimonials{position:absolute;left:0;top:2881px;width:1200px;height:396px;background:linear-gradient(180deg,#b8441d 0%,#c44b1f 50%,#a63a1a 100%)}
.testimonials-photo{position:absolute;inset:0;background:radial-gradient(ellipse at 50% 70%,rgba(90,30,15,.35),transparent 55%)}
.testimonials h2{position:absolute;left:0;top:58px;width:1205px;text-align:center;color:var(--white);font-weight:700;font-size:34px}
.quote-text{position:absolute;left:280px;top:177px;width:650px;text-align:center;color:var(--white);font-size:19.5px;line-height:31px}
.author{position:absolute;left:0;top:280px;width:1205px;text-align:center;color:var(--white);font-family:'Mulish',sans-serif;font-weight:700;font-size:18px}

/* footer */
.site-footer{position:absolute;left:0;top:3277px;width:1200px;height:274px;background:var(--navy);color:var(--white)}
.site-footer .brand{left:0;width:1205px;justify-content:center;top:50px}
.site-footer .brand-mark{background:var(--white)}
.site-footer .brand-name{color:var(--white)}
.foot-nav{position:absolute;left:0;top:134px;width:1205px;display:flex;justify-content:center;gap:32px;font-size:15px;font-weight:600}
.copyright{position:absolute;left:0;top:164px;width:1205px;text-align:center;font-size:13px}
.social{position:absolute;left:0;top:207px;width:1205px;display:flex;justify-content:center;gap:34px}
.social span{width:22px;height:22px;border:2px solid var(--white);border-radius:50%}
</style>
</head>
<body>

<header class="site-header">
  <div class="brand"><span class="brand-mark"></span><span class="brand-name">VELO BROKERS</span></div>
  <nav class="nav"><span>ABOUT US</span><span>SERVICES</span><span>BEST CARS</span><span>VIDEOS</span><span>BLOG</span><span>CONTACT US</span></nav>
  <div class="phone">
    <svg width="16" height="16" viewBox="0 0 24 24"><path fill="#c4461b" d="M6.6 10.8a15 15 0 0 0 6.6 6.6l2.2-2.2a1 1 0 0 1 1-.25 11.4 11.4 0 0 0 3.6.57 1 1 0 0 1 1 1V20a1 1 0 0 1-1 1A17 17 0 0 1 3 4a1 1 0 0 1 1-1h3.5a1 1 0 0 1 1 1c0 1.25.2 2.45.57 3.57a1 1 0 0 1-.25 1z"/></svg>
    (555)-014-2290
  </div>
</header>

<section class="hero">
  <div class="hero-photo" role="img" aria-label="Silver SUV parked on a hill at sunset"></div>
  <h1 class="hero-title">WELCOME TO VELO BROKERS</h1>
  <p class="hero-sub">CAR BROKERING/CAR BUYING SERVICE</p>
  <div class="search">
    <div class="select" style="width:222px">New or Used<svg viewBox="0 0 14 14"><path d="M2 5l5 5 5-5" fill="none" stroke="#333" stroke-width="1.5"/></svg></div>
    <div class="select" style="width:167px">Select Make<svg viewBox="0 0 14 14"><path d="M2 5l5 5 5-5" fill="none" stroke="#333" stroke-width="1.5"/></svg></div>
    <div class="select" style="width:167px">Select Model<svg viewBox="0 0 14 14"><path d="M2 5l5 5 5-5" fill="none" stroke="#333" stroke-width="1.5"/></svg></div>
    <div class="btn-search btn">SEARCH</div>
  </div>
  <div class="hero-arrow" style="left:74px"><svg width="18" height="26" viewBox="0 0 18 26"><path d="M14 3L4 13l10 10" fill="none" stroke="#222" stroke-width="3"/></svg></div>
  <div class="hero-arrow" style="left:1066px"><svg width="18" height="26" viewBox="0 0 18 26"><path d="M4 3l10 10L4 23" fill="none" stroke="#222" stroke-width="3"/></svg></div>
  <svg class="hero-edge" width="1200" height="661" viewBox="0 0 1200 661">
    <polygon points="560,661 1200,584 1200,642" fill="#c4461b"/>
    <polygon points="0,661 1200,642 1200,661" fill="#ffffff"/>
  </svg>
</section>

<h2 class="sec-title" style="top:770px">ABOUT US</h2>
<div class="rule" style="left:572px;top:822px"></div>
<p class="about-text">Pellentesque faucibus Ut accumsan ultricies elit Maecenas at justo id velit placerat molestie Donec dictum lectus non odio Cras a ante vitae enim iaculis aliquam Mauris nunc quam venenatis nec euismod sit amet</p>

<div class="pale-band"></div>
<svg class="diamonds" width="1200" height="444" viewBox="0 0 1200 444" role="img" aria-label="Diamond tiles with car photos: new cars, used cars and car keys handover">
  <polygon points="267,0 489,222 267,444 45,222" fill="#3a4a72"/>
  <polygon points="936,0 1158,222 936,444 714,222" fill="#3a4a72"/>
  <polygon points="604,0 826,222 604,444 382,222" fill="#c4461b"/>
</svg>
<div class="tile" style="left:45px;top:1158px">
  <h3>NEW CARS</h3><p>Cras a ante vitae enim iaculis aliquam<br>Mauris nunc quam venenatis</p>
  <div class="down"><svg width="18" height="12" viewBox="0 0 18 12"><path d="M2 2l7 7 7-7" fill="none" stroke="#fff" stroke-width="2.5"/></svg></div>
</div>
<div class="tile" style="left:395px;top:1150px">
  <h3>USED CARS</h3><p>Cras a ante vitae enim iaculis aliquam<br>Mauris nunc quam venenatis</p>
  <div class="down" style="margin-top:16px"><svg width="18" height="12" viewBox="0 0 18 12"><path d="M2 2l7 7 7-7" fill="none" stroke="#fff" stroke-width="2.5"/></svg></div>
</div>
<div class="tile" style="left:726px;top:1150px">
  <h3>OUR SERVICES</h3><p>Cras a ante vitae enim iaculis aliquam<br>Mauris nunc quam venenatis</p>
  <div class="down"><svg width="18" height="12" viewBox="0 0 18 12"><path d="M2 2l7 7 7-7" fill="none" stroke="#fff" stroke-width="2.5"/></svg></div>
</div>

<h2 class="sec-title" style="top:1452px;color:var(--navy);font-weight:600;font-size:33px">OUR CARS</h2>
<div class="rule" style="left:573px;top:1497px"></div>
<svg class="slide-arrow" style="left:94px;top:1592px" width="26" height="50" viewBox="0 0 26 50"><path d="M24 2L3 25l21 23" fill="none" stroke="#222" stroke-width="2.5"/></svg>
<svg class="slide-arrow" style="left:1100px;top:1592px" width="26" height="50" viewBox="0 0 26 50"><path d="M2 2l21 23L2 48" fill="none" stroke="#222" stroke-width="2.5"/></svg>
<article class="car" style="left:146px"><div class="ph" role="img" aria-label="Blue hatchback" style="background:linear-gradient(180deg,#7aa6d6,#2f5fae 60%,#c8ccd2)"></div><h4>Your Car Title here</h4></article>
<article class="car" style="left:382px"><div class="ph" role="img" aria-label="Black sports coupe under a cloudy sky" style="background:linear-gradient(180deg,#d6dbe0,#8a9098 55%,#2a2c30)"></div><h4>Your Car Title here</h4></article>
<article class="car" style="left:617px"><div class="ph" role="img" aria-label="Blue crossover at sunset" style="background:linear-gradient(135deg,#f0a030,#c86a20 45%,#2f6aa8)"></div><h4>Your Car Title here</h4></article>
<article class="car" style="left:854px"><div class="ph" role="img" aria-label="Dark blue SUV on a wet road" style="background:linear-gradient(180deg,#e8eaee,#5a6f9a 50%,#1d2c52)"></div><h4>Your Car Title here</h4></article>

<section class="why">
  <div class="why-photo" role="img" aria-label="Happy driver in a car holding up a key and giving a thumbs up"></div>
  <h2>WHY CHOOSE US</h2>
  <div class="rule"></div>
  <p class="why-text">Pellentesque faucibus Ut accumsan ultricies elit Maecenas at justo id velit placerat molestie Donec dictum lectus non odio Cras a ante vitae enim iaculis aliquam Mauris nunc quam venenatis nec euismod sit amet eges</p>
  <div class="feature" style="left:668px;top:256px"><span class="ic"><svg width="20" height="20" viewBox="0 0 20 20"><circle cx="10" cy="10" r="9" fill="#fff"/><path d="M5.5 10l3 3 6-6" fill="none" stroke="#35405e" stroke-width="2.2"/></svg></span>EXTENDED<br>WARRANTY</div>
  <div class="feature" style="left:886px;top:256px"><span class="ic"><svg width="20" height="16" viewBox="0 0 20 16"><path d="M3 7l2-5h10l2 5v6H3z" fill="#fff"/><circle cx="6" cy="10" r="1.5" fill="#35405e"/><circle cx="14" cy="10" r="1.5" fill="#35405e"/></svg></span>COMPETITIVE<br>CAR FINANCE</div>
  <div class="feature" style="left:670px;top:335px"><span class="ic"><svg width="20" height="20" viewBox="0 0 20 20"><circle cx="10" cy="10" r="8" fill="none" stroke="#fff" stroke-width="2"/><path d="M10 5v5l3 2" fill="none" stroke="#fff" stroke-width="2"/></svg></span>WE HELP YOU<br>24/7</div>
  <div class="feature" style="left:888px;top:335px"><span class="ic"><svg width="14" height="22" viewBox="0 0 14 22"><text x="7" y="17" fill="#fff" font-size="18" font-family="Mulish,sans-serif" font-weight="700" text-anchor="middle">$</text></svg></span>BEST PRICE<br>GUARANTEE</div>
</section>

<h2 class="blogs-title">LATEST BLOGS</h2>
<div class="rule" style="left:156px;top:2417px"></div>
<article class="blog" style="left:153px">
  <div class="ph" role="img" aria-label="Couple signing papers with a car salesman" style="background:linear-gradient(135deg,#c23a2a,#e8d8cc 40%,#5d6470)"></div>
  <h4>Pellentesque faucibus Ut accumsan ultricies Maecenas</h4>
  <p>Duis quam Nam eget lacus Aliquam erat volutpat Quisque dignissim congue leo Mauris vel lacus vitae felis vestibulum</p>
  <div class="btn-read btn">READ MORE</div>
</article>
<article class="blog" style="left:457px">
  <div class="ph" role="img" aria-label="Young couple reviewing a car contract" style="background:linear-gradient(135deg,#2f3238,#c9b9a6 45%,#e9e4dd)"></div>
  <h4>Pellentesque faucibus Ut accumsan ultricies Maecenas</h4>
  <p>Duis quam Nam eget lacus Aliquam erat volutpat Quisque dignissim congue leo Mauris vel lacus vitae felis vestibulum</p>
  <div class="btn-read btn">READ MORE</div>
</article>
<article class="blog" style="left:762px">
  <div class="ph" role="img" aria-label="Car keys handed into an open hand" style="background:linear-gradient(135deg,#d6dde5,#8d98a6 50%,#2d333c)"></div>
  <h4>Pellentesque faucibus Ut accumsan ultricies Maecenas</h4>
  <p>Duis quam Nam eget lacus Aliquam erat volutpat Quisque dignissim congue leo Mauris vel lacus vitae felis vestibulum</p>
  <div class="btn-read btn">READ MORE</div>
</article>

<section class="testimonials">
  <div class="testimonials-photo" role="img" aria-label="Front of a car tinted in orange"></div>
  <h2>Testimonials</h2>
  <svg class="abs" style="left:574px;top:122px" width="58" height="46" viewBox="0 0 58 46"><path d="M4 46V26C4 12 12 4 24 2v8c-6 2-9 6-9 12h9v24zM34 46V26C34 12 42 4 54 2v8c-6 2-9 6-9 12h9v24z" fill="#e8b7a6"/></svg>
  <p class="quote-text">Sed ut perspiciatis unde omnis iste natus error sit voluptatem accusantium doloremque laudantium, totam rem aperiam, eaque ipsa quae ab illo inventore veritatis et quasi architecto beatae</p>
  <p class="author">JORDAN HALE</p>
  <svg class="abs" style="left:168px;top:200px" width="26" height="50" viewBox="0 0 26 50"><path d="M24 2L3 25l21 23" fill="none" stroke="#fff" stroke-width="2.5"/></svg>
  <svg class="abs" style="left:996px;top:200px" width="26" height="50" viewBox="0 0 26 50"><path d="M2 2l21 23L2 48" fill="none" stroke="#fff" stroke-width="2.5"/></svg>
</section>

<footer class="site-footer">
  <div class="brand"><span class="brand-mark"></span><span class="brand-name">VELO BROKERS</span></div>
  <nav class="foot-nav"><span>HOME</span><span>ABOUT US</span><span>SERVICES</span><span>BEST CARS</span><span>VIDEOS</span><span>BLOG</span><span>CONTACT US</span></nav>
  <p class="copyright">© 2019 Company Name&nbsp; All right reserved</p>
  <div class="social" aria-label="Social links"><span></span><span></span><span></span><span></span></div>
</footer>

</body>
</html>
```